12" Touchscreen Interface Graphic Design

We have a touchscreen control system already designed with rudimentary graphics. The functionality is there, we need to make the graphics look more professional.
The new graphics design is to be 'modular' so that things can be moved within the touchscreen software.
By modular i mean that i need to for example add or remove pumps from the system, change the piping layout, move location of the various graphical elements.
I have enough graphics skills to be able to re-size, stretch, colorize the submitted design to adapt it specifically to the ongoing changing needs of the interface.
I can "cut up" the submitted design to make my individual graphical elements (for example 80x100px image for the pump) that i can then move around where i want for future systems that have different hardware configurations.
Attached are screenshots of how the interface looks at the moment, with some comments on the side.
The graphical elements need ideally to have the same pixel dimensions as on the screenshot. If changes are recommended for a specific reason, each element within the overall display should have dimensions in increments of 10px
Also attached is a screenshot from one of our other unrelated control systems that has a graphics style we would like to be close to.
Look and feel
Each slider illustrates characteristics of the customer's brand and the style your logo design should communicate.

```html
<!DOCTYPE html>
<html lang="en">
<head>
<meta charset="utf-8">
<title>Chiller Plant Control Panel</title>
<link href="https://fonts.googleapis.com/css2?family=Share+Tech+Mono&family=Source+Sans+3:wght@400;600&display=swap" rel="stylesheet">
<style>
  :root {
    --panel: #4a8cc9;
    --pipe-supply: #7dcdf2;
    --pipe-return: #ffffff;
    --status-green: #1fae4b;
    --status-navy: #2e3a8f;
    --action-orange: #f7941d;
    --button-blue: #1a6bb5;
    --enable-blue: #80cff5;
    --frame: #8fc3ea;
    --text-light: #ffffff;
    --text-soft: #dcefff;
  }
  html, body { margin: 0; padding: 0; background: #ffffff; overflow: hidden; }
  .screen { display: block; width: 1200px; height: 848px; }
  .mono { font-family: "Share Tech Mono", monospace; fill: var(--text-light); }
  .sans { font-family: "Source Sans 3", sans-serif; fill: var(--text-light); }
  .panel-bg { fill: var(--panel); }
  .pipe-supply { stroke: var(--pipe-supply); stroke-width: 10; fill: none; }
  .pipe-return { stroke: var(--pipe-return); stroke-width: 8; fill: none; }
  .arrow-supply { fill: var(--pipe-supply); }
  .arrow-return { fill: var(--pipe-return); }
  .readout { fill: var(--panel); stroke: var(--frame); stroke-width: 2; }
  .action { fill: var(--action-orange); }
  .hours-tag { fill: var(--panel); stroke: var(--text-light); stroke-width: 1.5; stroke-dasharray: 4 3; }
  .pump-art { fill: #6fb6e6; }
  .chiller-head { fill: var(--panel); stroke: var(--frame); stroke-width: 2; }
  .chiller-green { fill: var(--status-green); }
  .chiller-navy { fill: var(--status-navy); stroke: var(--frame); stroke-width: 2; }
  .dash { stroke: var(--text-light); stroke-width: 1.5; stroke-dasharray: 4 3; fill: none; }
  .enable-box { fill: var(--enable-blue); }
  .config-box { fill: none; stroke: var(--frame); stroke-width: 2; }
  .step-btn { fill: var(--button-blue); }
  .valve-open { fill: var(--status-green); }
  .valve-closed { fill: var(--text-light); }
</style>
</head>
<body>
<svg class="screen" viewBox="0 0 1684 1190" xmlns="http://www.w3.org/2000/svg">
  <defs>
    <g id="chiller-unit">
      <rect class="chiller-head" x="0" y="0" width="104" height="53"/>
      <rect class="chiller-head" x="104" y="0" width="104" height="53"/>
      <text class="sans" x="52" y="36" font-size="27" text-anchor="middle">12.1°C</text>
      <text class="sans" x="156" y="36" font-size="27" text-anchor="middle">12.1°C</text>
      <rect class="chiller-green" x="0" y="53" width="208" height="72"/>
      <path class="dash" d="M0 53 H208 M0 78 H208 M0 102 H208 M104 53 V102"/>
      <text class="mono" x="92" y="71" font-size="16" text-anchor="end">1 HP!!!</text>
      <text class="mono" x="92" y="96" font-size="16" text-anchor="end">LP!!!</text>
      <text class="mono" x="200" y="71" font-size="16" text-anchor="end">12.1 BAR</text>
      <text class="mono" x="200" y="96" font-size="16" text-anchor="end">12.1 BAR</text>
      <text class="mono" x="104" y="122" font-size="16" text-anchor="middle">FREEZE STOP</text>
      <rect class="chiller-navy" x="0" y="125" width="208" height="78"/>
      <text class="mono" x="104" y="151" font-size="16" text-anchor="middle">ENABLED</text>
      <text class="mono" x="104" y="186" font-size="16" text-anchor="middle">PRESS TO INHIBIT</text>
      <path class="chiller-green" d="M0 203 H208 V223 Q208 263 168 263 H40 Q0 263 0 223 Z"/>
      <path class="dash" d="M0 210 H208"/>
      <rect class="dash" x="52" y="238" width="104" height="24"/>
      <text class="mono" x="104" y="256" font-size="16" text-anchor="middle">12345 hrs</text>
    </g>
    <g id="feed-arrows">
      <path class="arrow-supply" d="M27 0 L52 23 H2 Z"/>
      <path class="arrow-return" d="M130 23 L155 -3 H105 Z"/>
    </g>
  </defs>

  <rect class="panel-bg" x="0" y="80" width="1684" height="1030"/>

  <!-- supply header -->
  <g class="supply-line">
    <path class="pipe-supply" d="M0 180 H1295 M712 180 V265 M1002 180 V265 M1292 180 V265 M605 180 V628 H1295 M712 628 V712 M1002 628 V712 M1292 628 V712"/>
    <path class="arrow-supply" d="M500 180 L525 153 V207 Z"/>
    <rect class="readout" x="290" y="153" width="130" height="52"/>
    <text class="mono" x="355" y="189" font-size="30" text-anchor="middle">12.1°C</text>
  </g>

  <!-- return header -->
  <g class="return-line">
    <path class="pipe-return" d="M815 233 H1580 V1035 H500 M815 680 H1580 M815 233 V262 M1105 233 V262 M1395 233 V262 M815 680 V710 M1105 680 V710 M1395 680 V710"/>
    <g class="valve">
      <circle class="valve-closed" cx="1502" cy="232" r="24"/>
      <path class="valve-open" d="M1502 208 A24 24 0 0 1 1502 256 Z"/>
      <circle class="valve-closed" cx="1502" cy="680" r="24"/>
      <path class="valve-open" d="M1502 656 A24 24 0 0 1 1502 704 Z"/>
    </g>
  </g>

  <!-- sea water pump set -->
  <g class="pump-set">
    <path class="pipe-return" d="M110 340 H52 V470 M210 340 H265 V495 M210 495 H290 M420 495 H500 V865 H530"/>
    <path class="arrow-return" d="M553 495 L527 470 V520 Z M553 865 L527 840 V890 Z"/>
    <rect class="readout" x="290" y="470" width="130" height="50"/>
    <text class="mono" x="355" y="505" font-size="30" text-anchor="middle">12.1°C</text>
    <g role="img" aria-label="Sea water pump 1">
      <rect class="pump-art" x="110" y="240" width="100" height="118" rx="6"/>
      <text class="sans" x="157" y="352" font-size="26" font-weight="600" text-anchor="middle">1</text>
    </g>
    <g role="img" aria-label="Sea water pump 2">
      <rect class="pump-art" x="110" y="400" width="100" height="118" rx="6"/>
      <text class="sans" x="157" y="510" font-size="26" font-weight="600" text-anchor="middle">2</text>
    </g>
    <text class="mono" x="158" y="390" font-size="28" text-anchor="middle">SEA WATER</text>
    <rect class="hours-tag" x="107" y="206" width="105" height="24"/>
    <text class="mono" x="159" y="224" font-size="16" text-anchor="middle">12345 hrs</text>
    <rect class="hours-tag" x="107" y="522" width="105" height="24"/>
    <text class="mono" x="159" y="540" font-size="16" text-anchor="middle">12345 hrs</text>
    <rect class="action" x="0" y="207" width="105" height="78"/>
    <text class="sans" x="12" y="240" font-size="24">RESET</text>
    <text class="sans" x="12" y="269" font-size="24">HOURS</text>
    <rect class="action" x="0" y="470" width="105" height="78"/>
    <text class="sans" x="12" y="505" font-size="24">RESET</text>
    <text class="sans" x="12" y="534" font-size="24">HOURS</text>
    <rect class="action" x="290" y="338" width="157" height="77"/>
    <text class="sans" x="368" y="363" font-size="24" text-anchor="middle">CHANGE</text>
    <text class="sans" x="368" y="385" font-size="24" text-anchor="middle">SEA WATER</text>
    <text class="sans" x="368" y="408" font-size="24" text-anchor="middle">PUMP</text>
  </g>

  <!-- system controls -->
  <rect class="enable-box" x="27" y="562" width="263" height="130"/>
  <text class="mono" x="158" y="620" font-size="29" text-anchor="middle" style="fill:var(--text-soft)">SYSTEM ENABLE</text>
  <text class="mono" x="158" y="650" font-size="29" text-anchor="middle" style="fill:var(--text-soft)">SWITCH OFF</text>
  <rect class="config-box" x="317" y="562" width="130" height="130"/>
  <text class="mono" x="382" y="614" font-size="15" text-anchor="middle">SHOW SYSTEM</text>
  <text class="mono" x="382" y="631" font-size="15" text-anchor="middle">CONFIG</text>
  <text class="mono" x="382" y="648" font-size="15" text-anchor="middle">BOTTONS</text>

  <!-- circulation pump set -->
  <g class="pump-set">
    <path class="pipe-return" d="M110 880 H52 V1010 M210 880 H268 V1035"/>
    <path class="arrow-return" d="M522 1035 L500 1010 V1060 Z"/>
    <g role="img" aria-label="Circulation pump 1">
      <rect class="pump-art" x="110" y="780" width="100" height="118" rx="6"/>
      <text class="sans" x="157" y="890" font-size="26" font-weight="600" text-anchor="middle">1</text>
    </g>
    <g role="img" aria-label="Circulation pump 2">
      <rect class="pump-art" x="110" y="940" width="100" height="118" rx="6"/>
      <text class="sans" x="157" y="1050" font-size="26" font-weight="600" text-anchor="middle">2</text>
    </g>
    <text class="mono" x="158" y="930" font-size="28" text-anchor="middle">CIRCULATION</text>
    <rect class="hours-tag" x="107" y="746" width="105" height="24"/>
    <text class="mono" x="159" y="764" font-size="16" text-anchor="middle">12345 hrs</text>
    <rect class="hours-tag" x="107" y="1062" width="105" height="24"/>
    <text class="mono" x="159" y="1080" font-size="16" text-anchor="middle">12345 hrs</text>
    <rect class="action" x="0" y="747" width="105" height="78"/>
    <text class="sans" x="12" y="781" font-size="24">RESET</text>
    <text class="sans" x="12" y="810" font-size="24">HOURS</text>
    <rect class="action" x="0" y="1010" width="105" height="78"/>
    <text class="sans" x="12" y="1044" font-size="24">RESET</text>
    <text class="sans" x="12" y="1073" font-size="24">HOURS</text>
    <rect class="action" x="290" y="878" width="157" height="77"/>
    <text class="sans" x="368" y="903" font-size="24" text-anchor="middle">CHANGE</text>
    <text class="sans" x="368" y="925" font-size="24" text-anchor="middle">SEA WATER</text>
    <text class="sans" x="368" y="948" font-size="24" text-anchor="middle">PUMP</text>
  </g>

  <!-- setpoint and mode bar -->
  <rect class="readout" x="290" y="1010" width="130" height="46"/>
  <text class="mono" x="355" y="1044" font-size="30" text-anchor="middle">12.1°C</text>
  <rect class="step-btn" x="212" y="1037" width="78" height="73"/>
  <text class="sans" x="248" y="1080" font-size="24" text-anchor="middle">-</text>
  <rect class="readout" x="290" y="1058" width="130" height="50"/>
  <text class="mono" x="355" y="1082" font-size="16" text-anchor="middle">TARGET</text>
  <text class="mono" x="355" y="1101" font-size="16" text-anchor="middle">12°C</text>
  <rect class="step-btn" x="422" y="1037" width="78" height="73"/>
  <text class="sans" x="463" y="1080" font-size="24" text-anchor="middle">+</text>
  <path class="dash" d="M502 1110 V1062 H1080"/>
  <text class="mono" x="842" y="1096" font-size="30" text-anchor="middle">SUMMER - COOLING MODE</text>
  <rect class="action" x="1080" y="1037" width="158" height="73"/>
  <text class="sans" x="1158" y="1071" font-size="20" text-anchor="middle">CHANGE TO</text>
  <text class="sans" x="1158" y="1089" font-size="20" text-anchor="middle">HEATING MODE</text>

  <!-- chillers -->
  <g class="chiller-bank">
    <use href="#feed-arrows" x="685" y="262"/>
    <use href="#feed-arrows" x="975" y="262"/>
    <use href="#feed-arrows" x="1265" y="262"/>
    <use href="#feed-arrows" x="685" y="710"/>
    <use href="#feed-arrows" x="975" y="710"/>
    <use href="#feed-arrows" x="1265" y="710"/>

    <use href="#chiller-unit" x="660" y="285"/>
    <text class="mono" x="764" y="513" font-size="16" text-anchor="middle">CHILLER #1</text>
    <use href="#chiller-unit" x="950" y="285"/>
    <text class="mono" x="1054" y="513" font-size="16" text-anchor="middle">CHILLER #2</text>
    <use href="#chiller-unit" x="1240" y="285"/>
    <text class="mono" x="1344" y="513" font-size="16" text-anchor="middle">CHILLER #3</text>
    <use href="#chiller-unit" x="660" y="733"/>
    <text class="mono" x="764" y="961" font-size="16" text-anchor="middle">CHILLER #4</text>
    <use href="#chiller-unit" x="950" y="733"/>
    <text class="mono" x="1054" y="961" font-size="16" text-anchor="middle">CHILLER #5</text>
    <use href="#chiller-unit" x="1240" y="733"/>
    <text class="mono" x="1344" y="961" font-size="16" text-anchor="middle">CHILLER #6</text>
  </g>
</svg>
</body>
</html>
```